Healthy living company needs logo / business card

We are looking for a business identity for our company that operates in the Health and Wellness area.
Our audience is those open to hearing about the links between ill health and chemicals in the home as well as how to boost their health naturally through nutrition. We show people how to eliminate those toxins and share the message with others.
We also work with and mentor people who want to build their own business, share the message and create a leveraged income.
Our business name is: Brivora
The tag line we have is: Simple Changes ยท Healthy Living
Output for the project is:
Logo and business card design (2 people on the card).
Our perspective is for a modern, natural, simple, clean design (web 2.0 feel) that will appeal to a broad age range and audience. It should feel professional but not formal. It should not seem medical.
The logo should not be a gradient nor overly complex. Colouring should only be one or two colours at most. They can be bright, we are tending to lean towards green for obvious reasons but open to your thoughts.
Simplicity is the key.
The business card needs to be two sided. We like having the logo and card details on the front and then reversed out on the back with the logo and name in white on the colour block.
Please see the attached card brief document about the card content.

```html
<!DOCTYPE html>
<html lang="en">
<head>
<meta charset="utf-8">
<title>Brivora Business Card</title>
<link rel="stylesheet" href="https://fonts.googleapis.com/css2?family=Carlito&family=Noto+Serif&display=swap">
<style>
  :root {
    --backdrop: #1e1a19;
    --leaf-green: #86c226;
    --paper: #ffffff;
  }
  * { margin: 0; padding: 0; box-sizing: border-box; }
  html, body {
    width: 1086px; height: 1200px; overflow: hidden;
    background: var(--backdrop);
  }
  .canvas { position: relative; width: 1086px; height: 1200px; }
  .card {
    position: absolute; left: 95px; width: 896px; height: 498px;
    display: flex;
  }
  .card--front { top: 82px; }
  .card--back { top: 618px; }
  .panel { position: relative; width: 448px; height: 100%; }
  .panel--green { background: var(--leaf-green); color: var(--paper); }
  .panel--white { background: var(--paper); }

  .contact {
    position: absolute; top: 68px; left: 0; width: 100%;
    text-align: center;
    font-family: "Noto Serif", serif;
    font-size: 26px; line-height: 31px; letter-spacing: 1.4px;
  }
  .contact__group { margin-bottom: 33px; }

  .brand {
    position: absolute; left: 0; width: 100%;
    text-align: center;
    font-family: "Carlito", sans-serif; font-weight: 400;
    font-size: 80px; line-height: 80px; letter-spacing: 4px;
    color: var(--leaf-green);
  }
  .card--front .brand { top: 205px; left: 16px; }
  .card--back .brand { top: 205px; left: -18px; }

  .benefits {
    position: absolute; top: 62px; left: 49px;
    list-style: none;
    font-family: "Carlito", sans-serif;
    font-size: 30px; line-height: 37.8px;
  }
</style>
</head>
<body>
<div class="canvas">
  <section class="card card--front">
    <div class="panel panel--green">
      <div class="contact">
        <p class="contact__group">Name<br>Cell : 000000 000000</p>
        <p class="contact__group">Name<br>Cell : 000000 000000</p>
        <p class="contact__group">Office Phone :<br>0000000000000000</p>
        <p class="contact__group">E-mail :<br>hello@livebrivora.com</p>
      </div>
    </div>
    <div class="panel panel--white">
      <div class="brand">brivora</div>
    </div>
  </section>

  <section class="card card--back">
    <div class="panel panel--white">
      <div class="brand">brivora</div>
    </div>
    <div class="panel panel--green">
      <ul class="benefits">
        <li>Multiple Streams of Income</li>
        <li>Financial Freedom</li>
        <li>Own my Own Business</li>
        <li>More Time</li>
        <li>Personal Development</li>
        <li>Health and Vitality</li>
        <li>Help Others</li>
        <li>Meet New People</li>
        <li>Retirement Plan</li>
        <li>Leave a Legacy</li>
      </ul>
    </div>
  </section>
</div>
</body>
</html>
```